We need a design for our security installation based business. Our name is K M Security Systems

We need a business card for a security installation based company. We want to look modern and professional. We would like our company logo used and the three main colours to be white, black and orange. We install intruder alarms, cctv and access control. Our preference would be to use the black/orange design on the front and orange/black on the back. Feel free to post variations.

Target Market(s)

Business owners, commercial property and large residential properties

Industry/Entity Type

Business

Contact Information for Business Card

Owen Pelham 07813 592 640

Liam Fenwick 07751 286 419

operations@kmsecuritysystems.co.uk

Intruder Alarms
CCTV
Access Control

Colors
f78f20
000000
ffffff

Requirements
Must have
• Must have the logo on the business card somewhere

```html
<!DOCTYPE html>
<html lang="en">
<head>
<meta charset="utf-8">
<title>K M Security Systems — Business Card</title>
<link rel="stylesheet" href="https://fonts.googleapis.com/css2?family=Orbitron:wght@500;700&family=Open+Sans:wght@400&display=swap">
<style>
  :root {
    --stage: #141414;
    --card-black: #0c0c0c;
    --orange: #e64a0c;
    --ink: #0a0a0a;
    --display: "Orbitron", sans-serif;
    --body: "Open Sans", sans-serif;
  }
  * { box-sizing: border-box; margin: 0; padding: 0; }
  html, body { width: 1200px; height: 800px; overflow: hidden; }
  body {
    background: var(--stage);
    position: relative;
  }
  .card {
    position: absolute;
    top: 245px;
    width: 500px;
    height: 310px;
    border-radius: 16px;
    overflow: hidden;
    background: var(--card-black);
    box-shadow: 0 18px 40px rgba(0,0,0,.55);
  }
  .card--front { left: 60px; }
  .card--back { left: 640px; }

  /* Front: black with orange details */
  .brand {
    position: absolute;
    top: 62px;
    left: 48px;
    display: flex;
    align-items: center;
    gap: 14px;
  }
  .brand__mark {
    width: 26px;
    height: 26px;
    background: var(--orange);
  }
  .brand__name {
    font-family: var(--display);
    font-weight: 700;
    font-size: 24px;
    letter-spacing: 1px;
    color: var(--orange);
    text-transform: uppercase;
  }
  .services {
    position: absolute;
    right: 100px;
    bottom: 58px;
    list-style: none;
    text-align: right;
    font-family: var(--display);
    font-weight: 500;
    font-size: 15px;
    line-height: 1.65;
    letter-spacing: 1.5px;
    color: var(--orange);
    text-transform: uppercase;
  }
  .tab {
    position: absolute;
    right: 0;
    bottom: 70px;
    width: 62px;
    height: 62px;
  }

  /* Back: orange block with black notch and bottom strip */
  .split {
    position: absolute;
    inset: 0;
    background: var(--orange);
    clip-path: polygon(0 0, 66% 0, 66% 40%, 48% 62%, 48% 76%, 28% 76%, 28% 100%, 0 100%);
  }
  .contact {
    position: absolute;
    top: 40px;
    left: 24px;
    width: 290px;
    text-align: center;
    color: var(--ink);
  }
  .contact__name {
    font-family: var(--display);
    font-weight: 700;
    font-size: 19px;
    letter-spacing: 1px;
    text-transform: uppercase;
  }
  .contact__phone {
    margin-top: 8px;
    font-family: var(--display);
    font-weight: 500;
    font-size: 16px;
    letter-spacing: 1px;
  }
  .contact__email {
    margin-top: 16px;
    font-family: var(--body);
    font-size: 12px;
  }
  .back-brand {
    position: absolute;
    right: 26px;
    top: 140px;
    width: 150px;
    text-align: right;
    font-family: var(--display);
    font-weight: 700;
    font-size: 15px;
    line-height: 1.3;
    color: var(--orange);
    text-transform: uppercase;
  }
  .website {
    position: absolute;
    right: 22px;
    bottom: 26px;
    font-family: var(--display);
    font-weight: 500;
    font-size: 12px;
    letter-spacing: 0.5px;
    color: var(--orange);
    text-transform: uppercase;
    white-space: nowrap;
  }
</style>
</head>
<body>

  <section class="card card--front" aria-label="Business card front">
    <div class="brand">
      <span class="brand__mark"></span>
      <span class="brand__name">K M Security Systems</span>
    </div>
    <ul class="services">
      <li>Intruder Alarms</li>
      <li>CCTV</li>
      <li>Access Control</li>
    </ul>
    <svg class="tab" viewBox="0 0 62 62" aria-hidden="true">
      <polygon points="20,0 62,0 62,62 20,62 0,31" fill="var(--orange)"/>
    </svg>
  </section>

  <section class="card card--back" aria-label="Business card back">
    <div class="split"></div>
    <div class="contact">
      <p class="contact__name">Owen Pelham</p>
      <p class="contact__phone">07813 592 640</p>
      <p class="contact__email">operations@kmsecuritysystems.co.uk</p>
    </div>
    <p class="back-brand">K M Security Systems</p>
    <p class="website">www.kmsecuritysystems.co.uk</p>
  </section>

</body>
</html>
```